Bold, dynamic Brick paver/landscaping company flyer

I need a flyer of 11" long x 8.5" high advertising our brick paver installation service. I want it clean, elegant and bold. I tried to give a general idea of what i was looking for by creating a very poor version for you guys to begin with. That being said, i am no designer, which is why i need your help. You have complete artistic license, show me what you got! I will attach our logo, the photos i used in the mock up as well as the mock up of basic idea. I hate my fonts, i hate to colors of them, i hate the way the pictures overlap without any seperation, but i like the basic idea. Use your artistic vision and skill to transform into something with a flair that will leave my potential customers thinking i am the most upscale service in the area. Please dont hesitate to ask any questions.

all of this bieng said, if you have an awesome idea thats completely different, im not invested in this idea alone, i will consider all options equally. Thanks!

Target Market(s)

high end homes, wealthy clientle

Industry/Entity Type

Advertising

Requirements
Must have
• Must have the blank white box in the upper right corner of approximate size, doesnt have to be exact. the gopher should be removed as well. The text "local postal customer should be there at the bottom of the box.

Company Name, phone number and web address

I like the wording of the text in the upper left, but hate the look of it

```html
<!DOCTYPE html>
<html lang="en">
<head>
<meta charset="utf-8">
<title>Stoneleaf Landscaping – Paver Flyer</title>
<link rel="stylesheet" href="https://fonts.googleapis.com/css2?family=Kalam:wght@400;700&family=Asap+Condensed:wght@500&family=Asap:wght@500&display=swap">
<style>
  :root{
    --backdrop:#d9d9d9;
    --divider:#7b7b7b;
    --green-light:#34803a;
    --green-dark:#24602a;
    --paper:#ffffff;
    --ink:#2b2b2b;
    --text-light:#ffffff;
  }
  *{margin:0;padding:0;box-sizing:border-box}
  html,body{width:1200px;height:793px;overflow:hidden;background:var(--backdrop)}
  .flyer{
    position:absolute;left:120px;top:10px;width:960px;height:773px;
    background:var(--divider);overflow:hidden;
    box-shadow:0 2px 10px rgba(0,0,0,.25);
  }
  .photo{position:absolute}
  .photo--home{left:0;top:0;width:634px;height:317px;
    background:linear-gradient(160deg,#6f86a8 0%,#3f4f6a 30%,#2f3a33 55%,#8c7f70 80%,#6d6a66 100%)}
  .photo--walkway{left:0;top:400px;width:472px;height:373px;
    background:linear-gradient(170deg,#3a3530 0%,#7b6350 30%,#b59a80 60%,#9b8873 100%)}
  .photo--firepit{left:484px;top:400px;width:476px;height:373px;
    background:linear-gradient(180deg,#2d4a24 0%,#4f7a2e 22%,#8a8070 45%,#5b4b3e 70%,#a89a88 100%)}
  .mailing-box{position:absolute;left:646px;top:0;width:314px;height:190px;background:var(--paper)}
  .mailing-box__label{
    position:absolute;bottom:8px;width:100%;text-align:center;
    font-family:"Asap",sans-serif;font-size:17px;color:var(--ink)}
  .bands{position:absolute;left:0;top:0;width:960px;height:773px}
  .brand{position:absolute;left:0;top:317px;width:634px;height:130px;color:var(--text-light);
    font-family:"Kalam",cursive;text-shadow:1px 2px 2px rgba(0,0,0,.55)}
  .brand__name{position:absolute;left:38px;top:10px;font-size:40px;font-weight:700;letter-spacing:1px}
  .brand__web{position:absolute;right:26px;top:66px;font-size:21px;letter-spacing:1px}
  .brand__phone{position:absolute;right:26px;top:98px;font-size:22px;letter-spacing:1px}
  .tagline{position:absolute;left:650px;top:222px;width:310px;text-align:center;color:var(--text-light);
    font-family:"Asap Condensed",sans-serif;font-weight:500;font-size:29px;line-height:40px;letter-spacing:-.3px}
  .tagline p + p{margin-top:20px}
</style>
</head>
<body>
  <main class="flyer">
    <div class="photo photo--home" role="img" aria-label="Photo of a modern home at dusk with a lit paver driveway"></div>
    <div class="photo photo--walkway" role="img" aria-label="Photo of a curved paver patio with stone pillars"></div>
    <div class="photo photo--firepit" role="img" aria-label="Photo of a backyard paver patio with a fire pit and lounge chairs"></div>

    <div class="mailing-box">
      <span class="mailing-box__label">Local Postal Customer</span>
    </div>

    <svg class="bands" viewBox="0 0 960 773" aria-hidden="true">
      <defs>
        <linearGradient id="greenFill" x1="0" y1="0" x2="0" y2="1">
          <stop offset="0" stop-color="var(--green-light)"/>
          <stop offset="1" stop-color="var(--green-dark)"/>
        </linearGradient>
      </defs>
      <rect x="634" y="190" width="326" height="14" fill="var(--divider)"/>
      <path d="M0,317 H634 V204 H960 V410 Q480,528 0,412 Z" fill="url(#greenFill)"/>
      <path d="M0,412 Q480,528 960,410" fill="none" stroke="var(--divider)" stroke-width="10"/>
      <rect x="634" y="190" width="14" height="273" fill="var(--divider)"/>
      <rect x="0" y="315" width="634" height="4" fill="var(--divider)"/>
    </svg>

    <header class="brand">
      <h1 class="brand__name">Stoneleaf Landscaping</h1>
      <p class="brand__web">StoneleafLandscaping.com</p>
      <p class="brand__phone">(555)214-0387</p>
    </header>

    <section class="tagline">
      <p>Where the elegance<br>of pavers...</p>
      <p>Meets the beauty<br>of design..</p>
    </section>
  </main>
</body>
</html>
```